Lowell Brandt

20 Year Licensed Master Barber specializing in:
men/women cuts, Grooming, Straight razor Shaving and tape line enhancement, beard grooming, eye brow enhancement, South of France, Hot Towel Treatments, Scalp, Blow outs, Shags, Custom Design,RazorCuts,Shear Cuts, Bobs, Perms, Relaxers, Shoe Shine.
Please create a wonderful business card incorporating all the info above and selecting one of the photos. Please be creative.

Barber

```html
<!DOCTYPE html>
<html lang="en">
<head>
<meta charset="utf-8">
<title>Lowell Brandt – Master Barber Business Card</title>
<link rel="stylesheet" href="https://fonts.googleapis.com/css2?family=Roboto:wght@300;400;700&family=Noto+Serif:ital,wght@1,400;1,700&display=swap">
<style>
  :root {
    --stage: #e9e6e1;
    --paper: #ffffff;
    --navy: #2f3a8f;
    --navy-dark: #232c73;
    --red: #c8262d;
    --ink: #4a4a55;
    --back-bg: #0d0f14;
    --back-text: #f2f2f2;
    --photo-top: #2a2c31;
    --photo-bottom: #0b0c0f;
  }
  * { box-sizing: border-box; margin: 0; padding: 0; }
  html, body { width: 1200px; height: 950px; overflow: hidden; }
  body {
    background: var(--stage);
    font-family: "Roboto", Arial, sans-serif;
    display: flex;
    flex-direction: column;
    align-items: center;
    justify-content: center;
    gap: 50px;
  }
  .card {
    width: 700px;
    height: 400px;
    position: relative;
    overflow: hidden;
    box-shadow: 0 6px 18px rgba(0,0,0,0.18);
  }

  /* Front */
  .card-front { background: var(--paper); }
  .front-band {
    position: absolute; left: 0; right: 0; bottom: 0;
    height: 34px; background: var(--navy);
  }
  .front-rule {
    position: absolute; left: 0; right: 0; bottom: 40px;
    height: 3px; background: var(--red);
  }
  .brand-mark {
    position: absolute; left: 240px; top: 70px;
    width: 220px;
    display: flex; flex-direction: column; align-items: center; gap: 14px;
  }
  .brand-dot {
    width: 120px; height: 120px; border-radius: 50%;
    background: var(--navy);
  }
  .brand-name {
    font-weight: 700; font-size: 30px; color: var(--navy);
    letter-spacing: 1px; text-transform: uppercase;
  }
  .contact-list {
    position: absolute; left: 40px; bottom: 70px;
    list-style: none; display: flex; flex-direction: column; gap: 8px;
    font-weight: 300; font-size: 19px; color: var(--ink);
  }
  .contact-list li { display: flex; align-items: center; gap: 10px; }
  .contact-list svg { width: 18px; height: 18px; flex: none; }
  .social-list {
    position: absolute; right: 40px; top: 40px;
    list-style: none; display: flex; flex-direction: column; gap: 8px;
    align-items: flex-end;
    font-weight: 300; font-size: 19px; color: var(--ink);
  }
  .social-list li { display: flex; align-items: center; gap: 10px; }
  .social-square { width: 16px; height: 16px; background: var(--navy); }

  /* Back */
  .card-back { background: var(--back-bg); }
  .back-photo {
    position: absolute; right: 0; bottom: 0;
    width: 380px; height: 400px;
    background: linear-gradient(160deg, var(--photo-top), var(--photo-bottom));
  }
  .back-badge {
    position: absolute; left: 40px; top: 30px;
    display: flex; align-items: center; gap: 12px;
  }
  .back-badge .brand-dot { width: 46px; height: 46px; background: var(--paper); }
  .back-badge .brand-name { font-size: 20px; color: var(--back-text); }
  .services {
    position: absolute; left: 40px; top: 100px; width: 400px;
    font-family: "Noto Serif", Georgia, serif; font-style: italic;
    color: var(--back-text); font-size: 16px; line-height: 1.55;
  }
  .services-title { font-weight: 700; font-size: 18px; margin-bottom: 6px; }
</style>
</head>
<body>

  <section class="card card-front" aria-label="Business card front">
    <ul class="social-list">
      <li>lbrandtcuts <span class="social-square"></span></li>
      <li>Lowell.Brandt5 <span class="social-square"></span></li>
    </ul>

    <div class="brand-mark">
      <div class="brand-dot"></div>
      <div class="brand-name">Lowell Brandt</div>
    </div>

    <ul class="contact-list">
      <li>
        <svg viewBox="0 0 24 24" aria-hidden="true"><path fill="#2f3a8f" d="M6.6 10.8a15 15 0 0 0 6.6 6.6l2.2-2.2a1 1 0 0 1 1-.25 11.4 11.4 0 0 0 3.6.57 1 1 0 0 1 1 1V20a1 1 0 0 1-1 1A17 17 0 0 1 3 4a1 1 0 0 1 1-1h3.5a1 1 0 0 1 1 1c0 1.25.2 2.45.57 3.6a1 1 0 0 1-.25 1z"/></svg>
        (555) 310-4862
      </li>
      <li>
        <svg viewBox="0 0 24 24" aria-hidden="true"><rect x="2" y="5" width="20" height="14" fill="#2f3a8f"/><path d="M2 5l10 8 10-8" fill="none" stroke="#fff" stroke-width="1.6"/></svg>
        lowell.brandt@mailbox.test
      </li>
    </ul>

    <div class="front-rule"></div>
    <div class="front-band"></div>
  </section>

  <section class="card card-back" aria-label="Business card back">
    <div class="back-photo" role="img" aria-label="Portrait photo of the barber in a dark suit and bow tie"></div>

    <div class="back-badge">
      <div class="brand-dot"></div>
      <div class="brand-name">Lowell Brandt</div>
    </div>

    <div class="services">
      <p class="services-title">20 Year Licensed Master Barber specializing in</p>
      <p>men/women cuts, Grooming, Straight razor<br>
      Shaving and tape line enhancement<br>
      beard grooming, eye brow enhancement<br>
      South of France, Hot Towel Treatments<br>
      Scalp, Blow outs, Shags, Custom Design<br>
      Razor Cuts, Shear Cuts, Bobs, Perms</p>
    </div>
  </section>

</body>
</html>
```